Horticulture Consulting Company Premium Card

We are looking for new design for a premium business card.
Our cards will be printed on glossy and embossed premium card stock.

Target Market(s)

Horticulture business owners needing our consulting services

Contact Information for Business Card

Marcus Thorne
(555) 348-2916
Marcus@velturaq.com

Requirements
Must have
• Company Logo and Contact information.
• Some additional work to add interest to the card
Should not have
• Red or Yellow

```html
<!DOCTYPE html>
<html lang="en">
<head>
<meta charset="utf-8">
<title>Velturaq Solutions – Business Card</title>
<link href="https://fonts.googleapis.com/css2?family=Exo+2:ital,wght@1,800&family=Lato:wght@300;400;700;900&display=swap" rel="stylesheet">
<style>
  :root {
    --backdrop: #2b2b2c;
    --card: #1f1f20;
    --green: #3cb54a;
    --blue: #1b75c4;
    --ink: #e4e4e4;
    --muted: #b8b8b8;
    --emboss: #7c7c7e;
  }
  * { margin: 0; padding: 0; box-sizing: border-box; }
  html, body {
    width: 1200px; height: 900px; overflow: hidden;
    background: var(--backdrop);
    font-family: "Lato", sans-serif;
  }
  .sheet {
    position: relative; width: 1200px; height: 900px;
  }
  .card {
    position: absolute; left: 250px;
    width: 700px; height: 400px;
    background: var(--card);
    box-shadow: 0 10px 30px rgba(0,0,0,.45);
    overflow: hidden;
  }
  .card--front { top: 40px; }
  .card--back { top: 470px; }

  /* Front */
  .front-mark {
    position: absolute; left: 0; right: 0; top: 150px;
    display: flex; align-items: center; justify-content: center; gap: 18px;
  }
  .mark-dot {
    width: 74px; height: 74px; border-radius: 50%;
    border: 6px solid var(--emboss);
  }
  .front-mark .brand-name {
    font-family: "Lato", sans-serif; font-weight: 900;
    font-size: 40px; letter-spacing: 1px; color: var(--emboss);
    line-height: 1.05;
  }

  /* Back */
  .back-mark {
    position: absolute; right: 42px; top: 48px;
    display: flex; flex-direction: column; align-items: center; gap: 10px;
  }
  .back-mark .mark-dot {
    width: 64px; height: 64px; border: 6px solid var(--blue);
  }
  .back-mark .brand-name {
    font-weight: 900; font-size: 26px; color: var(--blue);
    text-align: center; line-height: 1.05; letter-spacing: .5px;
  }
  .person {
    position: absolute; left: 48px; top: 178px;
  }
  .person__name {
    font-family: "Exo 2", sans-serif; font-style: italic; font-weight: 800;
    font-size: 30px; color: var(--green); letter-spacing: 1px;
  }
  .person__role {
    font-weight: 300; font-size: 18px; color: var(--muted); letter-spacing: 1px;
    margin-top: 2px;
  }
  .divider {
    position: absolute; top: 258px; height: 2px;
  }
  .divider--blue { left: 44px; width: 430px; background: var(--blue); }
  .divider--green { left: 478px; width: 180px; background: var(--green); }
  .contacts {
    position: absolute; left: 44px; top: 282px;
    list-style: none; display: flex; flex-direction: column; gap: 12px;
  }
  .contacts li {
    display: flex; align-items: center; gap: 12px;
    font-size: 19px; font-weight: 400; color: var(--ink); letter-spacing: 1px;
  }
  .contacts svg { width: 18px; height: 18px; fill: var(--blue); }
  .website {
    position: absolute; right: 42px; top: 330px;
    font-size: 20px; color: var(--ink); letter-spacing: 1.5px;
  }
  .website .accent { color: var(--green); }
  .base-band {
    position: absolute; bottom: 0; height: 7px;
  }
  .base-band--green { left: 0; width: 450px; background: var(--green); }
  .base-band--blue { left: 452px; right: 0; background: var(--blue); }
</style>
</head>
<body>
<main class="sheet">
  <section class="card card--front" aria-label="Card front">
    <div class="front-mark">
      <span class="mark-dot"></span>
      <span class="brand-name">VELTURAQ<br>SOLUTIONS</span>
    </div>
  </section>

  <section class="card card--back" aria-label="Card back">
    <div class="back-mark">
      <span class="mark-dot"></span>
      <span class="brand-name">VELTURAQ<br>SOLUTIONS</span>
    </div>

    <div class="person">
      <h1 class="person__name">MARCUS THORNE</h1>
      <p class="person__role">Owner</p>
    </div>

    <span class="divider divider--blue"></span>
    <span class="divider divider--green"></span>

    <ul class="contacts">
      <li>
        <svg viewBox="0 0 18 18" aria-hidden="true"><path d="M5 1h8a1.5 1.5 0 0 1 1.5 1.5v13A1.5 1.5 0 0 1 13 17H5a1.5 1.5 0 0 1-1.5-1.5v-13A1.5 1.5 0 0 1 5 1zm0 2v10h8V3zm4 11a1 1 0 1 0 0 2 1 1 0 0 0 0-2z"/></svg>
        (555) 348-2916
      </li>
      <li>
        <svg viewBox="0 0 18 18" aria-hidden="true"><path d="M1 4h16v1L9 10 1 5zM1 7l8 5 8-5v8H1z"/></svg>
        Marcus@velturaq.com
      </li>
    </ul>

    <p class="website">www.<span class="accent">velturaq</span>.com</p>

    <span class="base-band base-band--green"></span>
    <span class="base-band base-band--blue"></span>
  </section>
</main>
</body>
</html>
```